Präsentationsvorlagen für Strahlenschutzkurse
Zielgruppe
Wir bieten Strahlenschutzkurse in der Medizin an. Zielgruppe: Ärztinnen und Ärzte
Stichworte: Erwachsenenbildung, wissenschaftliche Inhalte
Aufgabenstellung
Wir benötigen eine Power-Point Präsentationsvorlage für unsere Kurse.
Auf allen Folien:
*Integration von unserem Logo
*Übernahme unseres bestehenden Farbkonzepts
*Feld für Überschrift
*kleines Textfeld für die Angabe der jeweiligen Quelle
Wir benötigen:
eine Folie nur mit Textfeld (z.B. Aufzählung, kurzer Text)
eine Folie Text mit Bild
eine Folie Bild bzw. Video
eine Folie mit einem wichtigen Lehrinhalt (wichtiger Text) - besondere Vorhebung erwünscht
eine Folie für Anfang bzw. Ende
HEX-CODE:
#4f93fe
#eea62f
#ffffff

```html
<!DOCTYPE html>
<html lang="de">
<head>
<meta charset="utf-8">
<title>Herzlich Willkommen zum Strahlenschutzkurs</title>
<link rel="stylesheet" href="https://fonts.googleapis.com/css2?family=Open+Sans:wght@300;400&display=swap">
<style>
  :root {
    --ink-navy: #365a82;
    --accent-blue: #4f8ef0;
    --band-grey: #9aa6b4;
    --fade-grey: #e7eaee;
    --white: #ffffff;
  }
  * { margin: 0; padding: 0; box-sizing: border-box; }
  html, body { width: 1200px; height: 675px; overflow: hidden; background: var(--white); }
  .slide {
    position: relative;
    width: 1200px;
    height: 675px;
    overflow: hidden;
    font-family: "Open Sans", sans-serif;
    background: linear-gradient(to bottom, var(--white) 0px, var(--white) 390px, var(--fade-grey) 564px);
  }
  .corner-brand {
    position: absolute;
    top: 62px;
    right: 52px;
    display: flex;
    align-items: center;
    gap: 12px;
    color: var(--ink-navy);
    font-weight: 300;
    font-size: 20px;
    letter-spacing: 1px;
  }
  .corner-brand .brand-dot {
    width: 54px;
    height: 54px;
    border: 4px solid var(--ink-navy);
    border-radius: 50%;
  }
  .welcome {
    position: absolute;
    top: 232px;
    left: 0;
    width: 1228px;
    text-align: center;
    font-weight: 300;
    line-height: 1.05;
  }
  .welcome .welcome-line {
    display: block;
    font-size: 62px;
    color: var(--ink-navy);
  }
  .welcome .course-line {
    display: block;
    font-size: 57px;
    color: var(--accent-blue);
  }
  .footer-band {
    position: absolute;
    left: 0;
    bottom: 0;
    width: 1200px;
    height: 111px;
    background: var(--band-grey);
    color: var(--white);
  }
  .footer-brand {
    position: absolute;
    left: 30px;
    top: 44px;
    display: flex;
    align-items: center;
    gap: 8px;
    font-size: 15px;
    font-weight: 400;
    letter-spacing: 0.5px;
  }
  .footer-brand .brand-dot {
    width: 16px;
    height: 16px;
    border: 2px solid var(--white);
    border-radius: 50%;
  }
  .footer-url {
    position: absolute;
    left: 0;
    width: 1228px;
    top: 46px;
    text-align: center;
    font-size: 18px;
  }
  .page-number {
    position: absolute;
    right: 44px;
    top: 48px;
    font-size: 16px;
  }
</style>
</head>
<body>
  <main class="slide">
    <div class="corner-brand">
      <span>LUMERA</span>
      <span class="brand-dot"></span>
    </div>

    <h1 class="welcome">
      <span class="welcome-line">Herzlich Willkommen</span>
      <span class="course-line">zum Strahlenschutzkurs</span>
    </h1>

    <footer class="footer-band">
      <div class="footer-brand">
        <span class="brand-dot"></span>
        <span>LUMERA STRAHLENSCHUTZ</span>
      </div>
      <div class="footer-url">www.lumera-strahlenkurse.de</div>
      <div class="page-number">2</div>
    </footer>
  </main>
</body>
</html>
```